Reliable and clean label for a natural product!

We would like to have a label design for our CBD SOFT GEL CAPSULES . We are a business family and believe in the power of natural healing. In this label we would like to show a reliable, natural and feminine product mainly.

Font styles to use
Serif
Sans Serif

Colors

Designer to choose colors to be used in the design.

```html
<!DOCTYPE html>
<html lang="en">
<head>
<meta charset="utf-8">
<title>Verda CBD – Soft Gel Capsules Label</title>
<link rel="stylesheet" href="https://fonts.googleapis.com/css2?family=Roboto:wght@300;400;500;700&family=Roboto+Condensed:wght@400;700&family=PT+Serif:wght@400&display=swap">
<style>
  :root {
    --magenta: #b52a8e;
    --magenta-edge: #c54ba0;
    --sand: #c29f8e;
    --sand-text: #c9a38c;
    --olive-text: #45472f;
    --sage: #6f7e5d;
    --white: #ffffff;
    --page: #ffffff;
  }
  * { margin: 0; padding: 0; box-sizing: border-box; }
  html, body { width: 1200px; height: 1200px; overflow: hidden; background: var(--page); }
  .canvas { position: relative; width: 1200px; height: 1200px; }

  .label {
    position: absolute; left: 100px; top: 250px;
    width: 1000px; height: 700px; overflow: hidden;
  }
  .label-bg { position: absolute; inset: 0; }

  .side-title {
    position: absolute; left: 0; top: 0; width: 260px; height: 700px;
  }
  .side-title-text {
    position: absolute; left: 30px; bottom: 24px; height: 650px;
    writing-mode: vertical-rl; transform: rotate(180deg);
    font-family: "Roboto Condensed", sans-serif; color: var(--sand-text);
    text-transform: uppercase; white-space: nowrap;
  }
  .side-title-main { display: block; font-size: 100px; line-height: 1; font-weight: 700; letter-spacing: 1px; text-align: start; }
  .side-title-sub { display: block; font-size: 76px; line-height: 1; font-weight: 400; letter-spacing: 2px; margin-left: 8px; text-align: end; }

  .content { position: absolute; left: 260px; top: 0; width: 740px; height: 700px; text-align: center; }

  .brand-mark {
    position: absolute; left: 50%; top: 38px; width: 112px; height: 112px;
    margin-left: -56px; border: 3px solid var(--white); border-radius: 50%;
  }
  .brand-name {
    position: absolute; left: 0; right: 0; top: 168px;
    font-family: "Roboto", sans-serif; font-weight: 400; font-size: 66px;
    color: var(--white); letter-spacing: 1px;
  }

  .tagline {
    position: absolute; left: 0; right: 0; top: 325px;
    font-family: "Roboto", sans-serif; font-weight: 500; font-size: 36px; color: var(--olive-text);
  }
  .pill {
    position: absolute; left: 50%; top: 378px; transform: translateX(-50%);
    background: var(--sage); color: var(--white); border-radius: 6px;
    font-family: "Roboto", sans-serif; font-size: 18px; padding: 5px 16px; white-space: nowrap;
  }
  .spec {
    position: absolute; left: 0; right: 0; top: 432px;
    font-family: "PT Serif", serif; font-size: 25px; line-height: 1.2; color: var(--white);
  }
  .claims {
    position: absolute; left: 110px; top: 540px; text-align: left;
    font-family: "Roboto", sans-serif; font-weight: 700; font-size: 11.5px;
    line-height: 1.7; color: var(--white); text-transform: uppercase; letter-spacing: 0.3px;
  }
  .count-row { position: absolute; left: 110px; top: 612px; display: flex; align-items: center; gap: 16px; }
  .count {
    background: var(--sage); color: var(--white); font-family: "Roboto", sans-serif;
    font-size: 18px; padding: 5px 18px;
  }
  .weight { font-family: "PT Serif", serif; font-size: 20px; color: var(--white); }
</style>
</head>
<body>
<div class="canvas">
  <div class="label">
    <svg class="label-bg" width="1000" height="700" viewBox="0 0 1000 700">
      <rect width="1000" height="700" fill="var(--magenta)"/>
      <rect x="0" y="0" width="6" height="700" fill="var(--magenta-edge)"/>
      <path role="img" aria-label="Sand panel with geometric leaf pattern"
            d="M260 300 C 420 275, 560 345, 700 318 S 900 248, 1000 256 L1000 676 L260 676 Z"
            fill="var(--sand)"/>
      <path d="M260 300 C 420 275, 560 345, 700 318 S 900 248, 1000 256"
            fill="none" stroke="var(--white)" stroke-width="3"/>
    </svg>

    <div class="side-title">
      <div class="side-title-text">
        <span class="side-title-main">CBD Soft Gel</span>
        <span class="side-title-sub">Capsules</span>
      </div>
    </div>

    <div class="content">
      <div class="brand-mark"></div>
      <div class="brand-name">VERDA CBD</div>

      <div class="tagline">Power Of Natural Healing</div>
      <div class="pill">Restorative Supplement</div>
      <div class="spec">Full Spectrum<br>25 mg CBD per capsule</div>

      <div class="claims">
        Complete support for the mind, body and immune system<br>
        GMO &amp; gluten free ingredients
      </div>

      <div class="count-row">
        <span class="count">30 CAPSULES</span>
        <span class="weight">260g e</span>
      </div>
    </div>
  </div>
</div>
</body>
</html>
```